Legal Consultant: Book cover for "Silver Ridge Transitions" in Australia.

This project is for the desiign of the front cover of a book t be published in perfect bond (A5) and as an eBook.

The target readers are Australian law firm partners.

I am a lawyer and senior legal recruitment consultant specialisng in the recruitment of law firm partners. I have written a short book that advises law firm partners how to make a lateral move to another law firm. It's simply about recruitment at a senior level. The book sets out the steps to maximise the partner's opportunity to engage the services of a senior legal recruitment consultant and then identify suitable law firms, interview techniques and preparation. A key element in the book is the preparation of various documents to submit to potential law firms eg CV, business plan, financial performance.

I know the eBook design has to 'grab" the reader so the title will need to jump out at the reader.

Target Market(s)

Senior law firm partners in Australia

Industry/Entity Type

Graphic Design

Requirements
Must have
• The cover must also be suitable for eBook publication. Therefore it must stand out from competitive publications.
Nice to have
• A design suitable for senior professional services executves.
Should not have
• No cliches eg shaking hands, two men in suits, judge's gavel etc

```html
<!DOCTYPE html>
<html lang="en">
<head>
<meta charset="utf-8">
<title>A Partner's Guide: Managing Your Lateral Move</title>
<link rel="stylesheet" href="https://fonts.googleapis.com/css2?family=Anton&family=Archivo:wght@700&display=swap">
<style>
  :root {
    --cover-navy: #141a2c;
    --cover-navy-light: #2a3550;
    --cover-shadow: #07090f;
    --cover-desk: #4a2c22;
    --cover-desk-light: #6b4232;
    --band-grey: rgba(178, 178, 178, 0.82);
    --band-ink: #111111;
    --title-white: #f4f4f4;
    --title-grey: #c9c9c9;
    --author-white: #ffffff;
  }
  html, body {
    margin: 0;
    padding: 0;
    width: 846px;
    height: 1200px;
    overflow: hidden;
    background: #000;
  }
  .book-cover {
    position: relative;
    width: 846px;
    height: 1200px;
    overflow: hidden;
  }
  .cover-art {
    position: absolute;
    inset: 0;
    width: 846px;
    height: 1200px;
  }
  .cover-type {
    position: absolute;
    inset: 0;
    width: 846px;
    height: 1200px;
  }
  .series-label {
    font-family: "Anton", "Impact", sans-serif;
    font-size: 60px;
    fill: var(--band-ink);
  }
  .title-line {
    font-family: "Anton", "Impact", sans-serif;
    font-size: 176px;
    fill: url(#titleFill);
    filter: url(#longShadow);
  }
  .author-name {
    font-family: "Archivo", "Arial", sans-serif;
    font-weight: 700;
    font-size: 40px;
    fill: var(--author-white);
  }
</style>
</head>
<body>
<main class="book-cover">
  <svg class="cover-art" viewBox="0 0 846 1200" role="img" aria-label="Blurred photograph of a professional in a dark suit seated at a wooden desk, hands resting on the desk">
    <defs>
      <linearGradient id="sceneTone" x1="0" y1="0" x2="0.25" y2="1">
        <stop offset="0" stop-color="#0c1120"/>
        <stop offset="0.3" stop-color="#1b2438"/>
        <stop offset="0.55" stop-color="#161d2f"/>
        <stop offset="0.72" stop-color="#2a1c1c"/>
        <stop offset="0.85" stop-color="#4a2c22"/>
        <stop offset="1" stop-color="#5e3a2c"/>
      </linearGradient>
    </defs>
    <rect width="846" height="1200" fill="url(#sceneTone)"/>
  </svg>

  <svg class="cover-type" viewBox="0 0 846 1200">
    <defs>
      <linearGradient id="titleFill" x1="0" y1="0" x2="0" y2="1">
        <stop offset="0" stop-color="var(--title-white)"/>
        <stop offset="1" stop-color="var(--title-grey)"/>
      </linearGradient>
      <filter id="longShadow" x="-10%" y="-10%" width="130%" height="140%">
        <feGaussianBlur in="SourceAlpha" stdDeviation="6"/>
        <feOffset dx="14" dy="16" result="blur"/>
        <feFlood flood-color="#000" flood-opacity="0.55"/>
        <feComposite in2="blur" operator="in" result="shadow"/>
        <feMerge>
          <feMergeNode in="shadow"/>
          <feMergeNode in="SourceGraphic"/>
        </feMerge>
      </filter>
    </defs>

    <g class="series-band">
      <rect x="0" y="60" width="765" height="122" fill="var(--band-grey)"/>
      <text class="series-label" x="156" y="153" textLength="579" lengthAdjust="spacingAndGlyphs">A PARTNER’S GUIDE:</text>
    </g>

    <g class="book-title">
      <text class="title-line" x="74" y="412" textLength="685" lengthAdjust="spacingAndGlyphs">MANAGING</text>
      <text class="title-line" x="74" y="603" textLength="344" lengthAdjust="spacingAndGlyphs">YOUR</text>
      <text class="title-line" x="74" y="793" textLength="663" lengthAdjust="spacingAndGlyphs">LATERAL</text>
      <text class="title-line" x="74" y="978" textLength="410" lengthAdjust="spacingAndGlyphs">MOVE</text>
    </g>

    <text class="author-name" x="405" y="1137" textLength="412" lengthAdjust="spacingAndGlyphs">Daniel Hartley LL.B</text>
  </svg>
</main>
</body>
</html>
```